Business Card Design needed for start up company Pramora

In need of a new business card designed for a start up company based in Sydney, Pramora is a new start up innovative Company, our mission it to make property accessible for everyday Australian and to become the leading Real Estate platform in Australia. We want it to be fresh and clean.

Industry/Entity Type

Financial

Contact Information for Business Card

Section for Name
Section for Title

PRAMORA - Where Doors Open Wide
Mobile:
Direct:

Font styles to use
Sans Serif

Colors
33a6d7
0692cd
0255a3
ffffff

Requirements
Must have
• Logo, all business card details

```html
<!DOCTYPE html>
<html lang="en">
<head>
<meta charset="utf-8">
<title>Pramora Business Card</title>
<link rel="stylesheet" href="https://fonts.googleapis.com/css2?family=Nunito:wght@400;800;900&display=swap">
<style>
  :root {
    --sky: #33a6d7;
    --ocean: #0692cd;
    --navy: #1d4a82;
    --royal: #0255a3;
    --white: #ffffff;
    --backdrop: #ececec;
  }
  * { box-sizing: border-box; margin: 0; padding: 0; }
  html, body { width: 1200px; height: 1200px; overflow: hidden; }
  body {
    background: var(--backdrop);
    font-family: "Nunito", sans-serif;
    position: relative;
  }
  .card {
    position: absolute;
    left: 260px;
    width: 680px;
    height: 416px;
    border-radius: 20px;
    overflow: hidden;
    box-shadow: 6px 8px 12px rgba(0,0,0,0.28);
  }
  .card-front {
    top: 92px;
    background: linear-gradient(to bottom,
      #229bd4 0%, #2aa0d8 18%, #9fd0ef 32%, #ffffff 48%,
      #a4d3f0 64%, #2ea2d9 82%, #229bd4 100%);
  }
  .card-back {
    top: 692px;
    background: linear-gradient(to bottom,
      #229bd4 0%, #2aa0d8 12%, #8cc6ec 28%, #ffffff 50%,
      #d6ebf9 62%, #a8d5f1 68%);
  }
  .brand {
    position: absolute;
    display: flex;
    align-items: center;
    justify-content: center;
    color: var(--navy);
    font-weight: 900;
    white-space: nowrap;
    line-height: 1;
  }
  .brand-dot {
    border-radius: 50%;
    background: var(--ocean);
    flex: none;
  }
  .card-front .brand {
    left: 0; width: 100%; top: 138px; height: 140px;
    gap: 16px; font-size: 60px; letter-spacing: -0.5px;
  }
  .card-front .brand-dot { width: 140px; height: 140px; }
  .card-back .brand {
    left: 20px; width: 310px; top: 60px; height: 82px;
    gap: 10px; font-size: 36px; letter-spacing: -0.5px;
  }
  .card-back .brand-dot { width: 82px; height: 82px; }
  .tagline {
    position: absolute;
    left: 20px; width: 310px; top: 152px;
    text-align: center;
    color: var(--royal);
    font-size: 21px;
    white-space: nowrap;
  }
  .divider {
    position: absolute;
    left: 339px; top: 37px;
    width: 3px; height: 172px;
    background: var(--royal);
  }
  .identity {
    position: absolute;
    left: 350px; width: 282px; top: 88px;
    text-align: center;
    color: var(--navy);
    white-space: nowrap;
  }
  .identity-name { font-size: 25px; font-weight: 800; }
  .identity-title { font-size: 21px; margin-top: 12px; color: var(--royal); }
  .contact-band {
    position: absolute;
    left: 0; top: 282px;
    width: 100%; height: 97px;
    background: var(--navy);
  }
  .contact-band-bottom {
    position: absolute;
    left: 0; top: 379px;
    width: 100%; height: 37px;
    background: var(--sky);
  }
  .contact {
    position: absolute;
    top: 30px;
    display: flex;
    align-items: center;
    gap: 8px;
    color: var(--white);
    font-size: 21px;
  }
  .contact svg { width: 34px; height: 34px; flex: none; }
  .contact-address { left: 63px; }
  .contact-mobile { left: 289px; }
  .contact-direct { left: 503px; }
</style>
</head>
<body>
  <section class="card card-front">
    <div class="brand"><span class="brand-dot"></span><span>PRAMORA</span></div>
  </section>

  <section class="card card-back">
    <div class="brand"><span class="brand-dot"></span><span>PRAMORA</span></div>
    <p class="tagline">Where Doors Open Wide</p>
    <div class="divider"></div>
    <div class="identity">
      <p class="identity-name">Section for Name</p>
      <p class="identity-title">Section for Title</p>
    </div>
    <div class="contact-band">
      <div class="contact contact-address">
        <svg viewBox="0 0 34 34" fill="none" stroke="#fff" stroke-width="1.6">
          <circle cx="17" cy="17" r="16"/>
          <path d="M17 28 C12 21 10 17 10 13.5 A7 7 0 0 1 24 13.5 C24 17 22 21 17 28 Z" fill="#fff" stroke="none"/>
          <circle cx="17" cy="13.5" r="2.8" fill="var(--navy)" stroke="none"/>
        </svg>
        <span>Address</span>
      </div>
      <div class="contact contact-mobile">
        <svg viewBox="0 0 34 34" fill="none" stroke="#fff" stroke-width="1.6">
          <circle cx="17" cy="17" r="16"/>
          <rect x="11.5" y="7.5" width="11" height="19" rx="2"/>
          <line x1="11.5" y1="22" x2="22.5" y2="22"/>
          <circle cx="17" cy="24.3" r="1" fill="#fff"/>
        </svg>
        <span>Mobile</span>
      </div>
      <div class="contact contact-direct">
        <svg viewBox="0 0 34 34" fill="none" stroke="#fff" stroke-width="1.6">
          <circle cx="17" cy="17" r="16"/>
          <path d="M11 9 L14 8 L16 13 L14 14.5 C15 17.5 17 20 19.5 21.5 L21 19.5 L26 22 L25 25 C18 26 10 17 11 9 Z" fill="#fff" stroke="none"/>
        </svg>
        <span>Direct</span>
      </div>
    </div>
    <div class="contact-band-bottom"></div>
  </section>
</body>
</html>
```